依頼詳細
RPE歯科クリニック~行きます訪問歯科・送迎歯科~
のパンフレットを作成依頼致します。

1.パンフレットに使用したいデータ等がございません。以前使用していたパンフレットをPDFで添付いたしますのでご確認ください。添付エクセルデータがございます。こちらを参考にA4両面に収めてレイアウトしてください。

2. パンフレットは以前のパンフレットの(ピンク×水色、ピンク、水色)を希望しております。

3.1枚目の車のロゴはないので、作成いただいてもフリー素材でも結構ですのでお願い致します。

4.MAPは、添付フィル≪MAP_image≫をご確認ください。

5.仕上がりはA4両面イラストレーターデザインを希望いたします。フルカラーでお願いします。
サイズ
A4
ページ数
4ページ
希望イメージ
シンプル 複雑
単色 カラフル
暗い 明るい
日常 高級
遊び心 厳粛
未来的 伝統的
女性的 男性的
希望する色
赤系、水色系
納品ファイル
• イラストレーター形式 (.ai)
補足説明
修正致します

1.添付エクセルデータがございます。→PDFデータの為、文字おこしお願い致します。
医院名
RPE歯科クリニック
~行きます訪問歯科・送迎歯科~
パンフレットのカテゴリになっておりますが、
A4サイズ両面のチラシ作成依頼になります。

よろしくお願いいたします。
コンペ当選者を確約に変更いたしましたのでよろしくお願いいたします。

色使いや、歯を使ったイラストの可愛さと、全体的に見やすくバランスが良かったです。

たくさんのご提案ありがとうございました。 慣れない依頼にご提案くださり感謝しています。 また、機会がありましたら是非ご協力ください。 ありがとうございました。

```html
<!DOCTYPE html>
<html lang="ja">
<head>
<meta charset="utf-8">
<title>RPE歯科クリニック 訪問・送迎歯科</title>
<link href="https://fonts.googleapis.com/css2?family=M+PLUS+Rounded+1c:wght@400;500;700;800&family=Zen+Maru+Gothic:wght@500;700&display=swap" rel="stylesheet">
<style>
:root{
  --pink:#e8588c;
  --pink-soft:#fbd9e4;
  --pink-pale:#fdeef3;
  --blue:#4fbde6;
  --blue-deep:#2a9fd0;
  --sky:#cfeef9;
  --sky-pale:#eef9fd;
  --yellow:#f5c231;
  --ink:#4a4a4a;
  --white:#ffffff;
}
*{margin:0;padding:0;box-sizing:border-box}
html,body{width:849px;height:1200px;overflow:hidden}
body{font-family:"M PLUS Rounded 1c",sans-serif;color:var(--ink);background:var(--white)}
.flyer{position:relative;width:849px;height:1200px;overflow:hidden;
  background:linear-gradient(180deg,var(--sky-pale) 0%,#fff 22%,#fff 38%,var(--sky) 46%,#bfe7f6 100%)}
.leaves{position:absolute;border-radius:50%;background:radial-gradient(circle,#b9e39a 0%,rgba(185,227,154,0) 70%)}
.leaves.left{left:-80px;top:-90px;width:300px;height:240px}
.leaves.right{right:-60px;top:-80px;width:260px;height:200px}
.bubble{position:absolute;border-radius:50%}
.hero-art{position:absolute;left:612px;top:40px;width:222px;height:250px;border-radius:40px;z-index:1;
  background:linear-gradient(160deg,#f4f8fb 0%,#dbe6ee 60%,#c9d8e3 100%)}
.clinic-name{position:absolute;left:248px;top:66px;z-index:2;font-family:"Zen Maru Gothic",sans-serif;font-weight:700;font-size:30px;color:var(--blue-deep);letter-spacing:1px}
.headline{position:absolute;left:150px;top:106px;z-index:2;font-weight:800;color:var(--pink);line-height:1.2;white-space:nowrap}
.headline .l1{display:block;font-size:44px}
.headline .l2{display:block;font-size:44px;padding-left:100px}
.intro-label{position:absolute;left:85px;top:270px;width:248px;height:34px;background:var(--pink);color:#fff;
  font-weight:700;font-size:20px;line-height:34px;text-align:center;border-radius:3px}
.intro-text{position:absolute;left:90px;top:316px;width:700px;font-size:16.5px;line-height:1.75;font-weight:500}
.treat{position:absolute;left:38px;top:386px;width:780px;height:88px;display:flex;gap:10px}
.treat-label{width:64px;background:var(--pink);border-radius:8px;color:#fff;font-weight:700;font-size:16px;
  display:flex;align-items:center;justify-content:center;text-align:center;line-height:1.3}
.treat-item{flex:1;background:#fff;border:2px solid var(--pink-soft);border-radius:12px;display:flex;align-items:center;gap:10px;padding:0 10px}
.treat-item svg{flex:none}
.treat-item p{font-size:13px;line-height:1.45;font-weight:500}
.brush-art{position:absolute;left:0;top:1000px;width:76px;height:200px;border-radius:0 40px 0 0;z-index:1;
  background:linear-gradient(150deg,#9dd7ef 0%,#f3a6c2 100%);opacity:.75}
.flow{position:absolute;left:84px;top:552px;width:690px;height:598px;background:#fff;border-radius:28px;padding:34px 38px 0;z-index:2}
.flow-title{width:340px;margin:0 auto 22px;background:var(--blue);color:#fff;text-align:center;font-weight:700;font-size:18px;height:34px;line-height:34px}
.step{position:relative;height:78px;margin-bottom:18px;display:flex;align-items:center;
  background:linear-gradient(90deg,var(--pink-pale) 0%,var(--pink-soft) 100%)}
.step-num{width:54px;text-align:center;font-size:38px;font-weight:800;font-style:italic;color:var(--yellow)}
.step-name{width:200px;font-size:24px;font-weight:700;color:var(--pink)}
.step-body{flex:1;font-size:13px;line-height:1.6;padding-right:10px}
.step-body em{font-style:normal;color:var(--pink)}
.step::after{content:"";position:absolute;left:18px;bottom:-16px;border-left:12px solid transparent;border-right:12px solid transparent;border-top:12px solid var(--yellow)}
.step:last-child::after{display:none}
</style>
</head>
<body>
<main class="flyer">
  <div class="leaves left"></div>
  <div class="leaves right"></div>
  <span class="bubble" style="left:760px;top:470px;width:90px;height:90px;background:#fff7c9"></span>
  <span class="bubble" style="left:20px;top:560px;width:60px;height:60px;background:#fde2ec"></span>
  <span class="bubble" style="left:780px;top:900px;width:120px;height:120px;background:#e5f6fc"></span>
  <span class="bubble" style="left:640px;top:1120px;width:140px;height:140px;background:#fff4b8"></span>

  <div class="hero-art" role="img" aria-label="送迎車に乗った歯科医師と笑顔の歯のキャラクターのイラスト"></div>
  <div class="clinic-name">RPE歯科クリニック</div>
  <h1 class="headline"><span class="l1">行きます 訪問・送迎</span><span class="l2">歯科クリニック</span></h1>

  <div class="intro-label">訪問歯科診療とは</div>
  <p class="intro-text">介護施設やご自宅で寝たきりの方や歩行が困難で通院ができない方のもとへ歯科医師や歯科衛生士が訪問し、診療を行う医療サービスです。</p>

  <section class="treat">
    <div class="treat-label">治療<br>内容</div>
    <div class="treat-item">
      <svg width="40" height="40" viewBox="0 0 40 40"><path d="M10 8c4-3 8 0 10 0s6-3 10 0 2 12 0 16-3 10-5 10-3-7-5-7-3 7-5 7-3-6-5-10-4-13 0-16z" fill="none" stroke="var(--blue)" stroke-width="2.5"/></svg>
      <p>虫歯、<br>歯周病の治療、<br>予防</p>
    </div>
    <div class="treat-item">
      <svg width="40" height="40" viewBox="0 0 40 40"><path d="M6 16q14-12 28 0v6q-14 8-28 0z" fill="none" stroke="var(--blue)" stroke-width="2.5"/><path d="M12 16v5M20 14v6M28 16v5" stroke="var(--blue)" stroke-width="2"/></svg>
      <p>入れ歯の作成、<br>修理、調整</p>
    </div>
    <div class="treat-item">
      <svg width="40" height="40" viewBox="0 0 40 40"><ellipse cx="20" cy="20" rx="14" ry="10" fill="none" stroke="var(--blue)" stroke-width="2.5"/><path d="M10 20h20" stroke="var(--pink)" stroke-width="2.5"/></svg>
      <p>口腔ケアで<br>感染症予防</p>
    </div>
    <div class="treat-item">
      <svg width="40" height="40" viewBox="0 0 40 40"><path d="M8 18q12 14 24 0" fill="none" stroke="var(--blue)" stroke-width="2.5"/><path d="M14 22q6 6 12 0" fill="var(--pink-soft)" stroke="var(--pink)" stroke-width="2"/></svg>
      <p>お口のリハビリ</p>
    </div>
  </section>

  <div class="brush-art" role="img" aria-label="水色とピンクの歯ブラシのイラスト"></div>

  <section class="flow">
    <h2 class="flow-title">訪問診療の流れ</h2>
    <div class="step"><span class="step-num">1</span><span class="step-name">お申し込み</span><p class="step-body">お電話・FAXなどでお気軽にお申込みください。</p></div>
    <div class="step"><span class="step-num">2</span><span class="step-name">訪問日の調整</span><p class="step-body">ご希望に合わせて訪問日を決定します。</p></div>
    <div class="step"><span class="step-num">3</span><span class="step-name">無料検診</span><p class="step-body">お口の状態を診察します。<em>費用は一切かかりません。</em></p></div>
    <div class="step"><span class="step-num">4</span><span class="step-name">治療</span><p class="step-body">診療を開始します。<br>初診時・月初めは、<em>各種保険証が必要</em>になります。<br>1回の診療時間は30分程度です。</p></div>
    <div class="step"><span class="step-num">5</span><span class="step-name">今後のご相談</span><p class="step-body">定期検診やブラッシング等のアフターケアのために定期的にお伺いします。<br>定期検診の結果により治療を再開します。</p></div>
  </section>
</main>
</body>
</html>
```